Flyer-Design für Einzelhandel/Online-Shop für Werbetechnikzubehör
Zielgruppe
Wir sind ein Einzelhandel / Onlineshop für Werbetechnikzubehör. Plotterfolie, Plotter, DIY-Artikel. Wir kommen mitten aus dem Ruhrgebiet und unser Name verbindet das Plotten und unsere Herkunft. „Lindenschnittwerk“
Unsere Zielgruppe sind Kreative aus dem Bastel- / Nähbereich.
Aufgabenstellung
Wir legen wert auf die Verbindung zum Ruhrgebiet (Zechen und co.) Anbei stellen wir auch eine Datei zur Verfügung, die bereits auf unserem Auto und Gutscheinen implementiert ist. Gerne darf diese genutzt werden.
Wir legen Wert auf Gradlinigkeit und Übersichtlichkeit.
Unser Flyer soll ein A6 Format sein (Datenformat: 154 x 111 mm
3 mm Beschnitt) diesen wir mit einem Rabattcode versehen wollen.
Des Weiteren benötigen wir auch die Abbidung von Instagram / Facebook / Homepage.
Daher benötigen wir das Design natürlich auch in einem Bearbeitungsmodus für ai.
Gerade die Felder Rabattcode und Gutscheinbedingungen sollten beachtet werden.
10% auf alle Vinyl, Flex & Flockfolie (Bogenware)
Der Flyer wird als Versandbeileger für befreundete Unternehmen benötigt.
Wir möchten mit diesem Flyer Neukunden gewinnen.
Der Flyer kann beidseitig gestaltet werden. Hoch oder Quer ist auch frei wählbar.
Unsere Farben sind als Datei hochgeladen.

```html
<!DOCTYPE html>
<html lang="de">
<head>
<meta charset="utf-8">
<title>Lindenschnittwerk – Rabattcode Flyer</title>
<link rel="stylesheet" href="https://fonts.googleapis.com/css2?family=Arimo:wght@400;700&display=swap">
<style>
  :root {
    --teal: #0099a8;
    --teal-light: #33aeb9;
    --ink: #231f20;
    --slate: #58595b;
    --paper: #ffffff;
    --text: #111111;
  }
  * { margin: 0; padding: 0; box-sizing: border-box; }
  html, body { width: 846px; height: 1200px; overflow: hidden; background: var(--paper); }
  body { font-family: "Arimo", Arial, sans-serif; color: var(--text); }
  .flyer { position: relative; width: 846px; height: 1200px; background: var(--paper); overflow: hidden; }
  .shapes { position: absolute; inset: 0; }
  .abs { position: absolute; white-space: nowrap; }

  .brand-mark { left: 195px; top: 72px; width: 44px; height: 44px; background: var(--teal); }
  .brand-name { left: 31px; top: 208px; font-size: 36px; font-weight: 400; color: var(--slate); letter-spacing: 0.5px; }

  .offer-title { color: var(--paper); font-size: 82px; font-weight: 400; line-height: 1; letter-spacing: -1px; }
  .offer-title.line1 { left: 524px; top: 222px; }
  .offer-title.line2 { left: 463px; top: 300px; }
  .offer-strip-text { left: 256px; top: 425px; color: var(--paper); font-size: 21.5px; font-weight: 700; letter-spacing: 0.1px; }

  .skyline { position: absolute; left: 0; top: 612px; width: 846px; height: 153px;
    background: linear-gradient(to bottom, rgba(51,174,185,0) 0%, rgba(51,174,185,0.25) 55%, rgba(51,174,185,0.55) 100%);
    border-bottom: 3px solid var(--teal-light); }

  .terms { position: absolute; left: 41px; top: 803px; width: 336px; }
  .terms h2 { font-size: 23px; font-weight: 400; color: var(--text); letter-spacing: -0.6px; line-height: 1; margin-bottom: 11px; }
  .terms p { font-size: 11.2px; line-height: 11.3px; text-align: justify; color: var(--text); }

  .social-handle { left: 691px; font-size: 18px; color: var(--paper); }
  .social-handle.insta { top: 856px; }
  .social-handle.fb { top: 925px; }

  .footer-name { left: 57px; top: 1012px; font-size: 21px; color: var(--slate); letter-spacing: 0.3px; }
  .footer-address { right: 495px; top: 1061px; text-align: right; color: var(--paper); font-size: 22px; line-height: 26px; }
  .contact-title { left: 558px; top: 1078px; color: var(--paper); font-size: 24px; }
  .contact-mail { left: 558px; top: 1114px; color: var(--paper); font-size: 17px; }
</style>
</head>
<body>
<main class="flyer">
  <svg class="shapes" width="846" height="1200" viewBox="0 0 846 1200" aria-hidden="true">
    <polygon class="offer-panel" points="541,162 846,162 846,399 381,399" fill="var(--teal)"/>
    <polygon class="offer-strip" points="258,399 846,399 846,469 184,469" fill="var(--ink)"/>

    <polygon class="social-icon-box" points="586,846 638,846 663,888 586,888" fill="var(--slate)"/>
    <polygon class="social-handle-bar" points="652,846 846,846 846,888 680,888" fill="var(--slate)"/>
    <circle cx="614" cy="867" r="9" fill="none" stroke="var(--paper)" stroke-width="2.5"/>

    <polygon class="social-icon-box" points="586,915 638,915 663,956 586,956" fill="var(--slate)"/>
    <polygon class="social-handle-bar" points="652,915 846,915 846,956 680,956" fill="var(--slate)"/>
    <circle cx="614" cy="935" r="9" fill="none" stroke="var(--paper)" stroke-width="2.5"/>

    <polygon class="contact-band" points="473,1044 846,1044 846,1157 421,1157" fill="var(--slate)"/>
    <polygon class="address-band" points="0,984 428,984 509,1131 0,1131" fill="var(--teal)"/>
    <line class="address-rule" x1="57" y1="1047" x2="351" y2="1047" stroke="var(--paper)" stroke-width="2"/>
  </svg>

  <div class="abs brand-mark" aria-hidden="true"></div>
  <div class="abs brand-name">LINDENSCHNITTWERK</div>

  <div class="abs offer-title line1">RABATT</div>
  <div class="abs offer-title line2">CODE</div>
  <div class="abs offer-strip-text">10 % AUF ALLE VINYL, FLEX - &amp; FLOCKFOLIEN</div>

  <div class="skyline" role="img" aria-label="Skyline-Silhouette des Ruhrgebiets mit Fördertürmen, Tetraeder, Achterbahn, Windrad und Fernsehturm"></div>

  <section class="terms">
    <h2>GUTSCHEINBEDINGUNGEN</h2>
    <p>Etiam ac augue. Morbi tincidunt neque ut lacus. Duis vulputate cursus orci. Mauris justo lorem, scelerisque sit amet, placerat sed, condimentum in, leo. Donec urna est, semper quis, auctor eget, ultrices in, purus. Etiam rutrum. Aliquam blandit dui a libero. Praesent tortor tortor, bibendum vehicula, accumsan sed, adipiscing a, pede. Nullam et tortor. Suspendisse tempor leo quis nunc</p>
  </section>

  <div class="abs social-handle insta">/lindenschnittwerk</div>
  <div class="abs social-handle fb">/lindenschnittwerk</div>

  <div class="abs footer-name">LINDENSCHNITTWERK</div>
  <address class="abs footer-address" style="font-style:normal">Kanalstraße 77<br>45139 Essen</address>

  <div class="abs contact-title">Schreib uns</div>
  <div class="abs contact-mail">tach@lindenschnittwerk.de</div>
</main>
</body>
</html>
```